Life Coach for Lawyers Business Card Design

Elegant, original, business card design for life coaching service for associate attorneys who work in big law and struggle with stress, overwhelm, and time management. Double sided design.

Target Market(s)

Women associate attorneys who work in big law and struggle with stress, overwhelm, and time management.

Industry/Entity Type

Life Coaching

Contact Information for Business Card

Marissa Pendrell
Life Coach
518.677.3941
calmbriefcounsel.net
marissa@calmbriefcounsel.net
@calmbriefcounsel (Instagram)

Font styles to use
Other font styles liked:
• Silver South font duo. See uploaded files.

Requirements
Must have
• Icons for phone, website, email, and Instagram instead of words. Specific colors used in my logo (171B2B, 421121, FFFFFF)
Nice to have
• Foil. Embossed. Feminine design.
Should not have
• Any colors other than those used in logo. See uploaded files.

```html
<!DOCTYPE html>
<html lang="en">
<head>
<meta charset="utf-8">
<title>Calm Brief Counsel – Business Cards</title>
<link href="https://fonts.googleapis.com/css2?family=Montserrat:wght@400;600;700&family=Playfair+Display:wght@400&display=swap" rel="stylesheet">
<style>
  :root {
    --burgundy: #421121;
    --ink: #171B2B;
    --white: #FFFFFF;
    --backdrop: #ECECEC;
    --text-grey: #3a3a3f;
  }
  * { margin: 0; padding: 0; box-sizing: border-box; }
  html, body {
    width: 1200px; height: 800px; overflow: hidden;
    background: var(--backdrop);
  }
  .canvas { position: relative; width: 1200px; height: 800px; }

  .card {
    position: absolute; top: 278px;
    width: 419px; height: 240px;
  }
  .card--front { left: 142px; background: var(--burgundy); }
  .card--back { left: 638px; background: var(--white); }

  .front-brand {
    position: absolute; inset: 0;
    display: flex; align-items: center; justify-content: center;
    font-family: "Playfair Display", serif;
    font-weight: 400; font-size: 34px; letter-spacing: 0.5px;
    color: var(--white);
  }

  .holder-name {
    position: absolute; left: 44px; top: 54px;
    font-family: "Montserrat", sans-serif; font-weight: 700;
    font-size: 21px; letter-spacing: 0.6px;
    color: var(--burgundy); text-transform: uppercase;
  }
  .holder-title {
    position: absolute; left: 46px; top: 81px;
    font-family: "Montserrat", sans-serif; font-weight: 600;
    font-size: 12.5px; letter-spacing: 0.6px;
    color: var(--burgundy); text-transform: uppercase;
  }

  .contact-list {
    position: absolute; left: 44px; top: 126px;
    list-style: none;
  }
  .contact-item {
    display: flex; align-items: center; gap: 9px;
    height: 18.5px;
    font-family: "Montserrat", sans-serif; font-weight: 400;
    font-size: 13px; color: var(--text-grey);
  }
  .contact-icon { width: 12px; height: 12px; flex: none; }

  .seal {
    position: absolute; left: 305px; top: 46px;
    width: 78px; height: 78px; border-radius: 50%;
    border: 1px solid var(--burgundy);
    display: flex; align-items: center; justify-content: center;
    text-align: center;
    font-family: "Playfair Display", serif; font-weight: 400;
    font-size: 10px; line-height: 1.25; color: var(--burgundy);
  }
</style>
</head>
<body>
<main class="canvas">

  <section class="card card--front" aria-label="Card front">
    <div class="front-brand">Calm Brief Counsel</div>
  </section>

  <section class="card card--back" aria-label="Card back">
    <h1 class="holder-name">Marissa Pendrell</h1>
    <p class="holder-title">Life Coach</p>

    <ul class="contact-list">
      <li class="contact-item">
        <svg class="contact-icon" viewBox="0 0 12 12" aria-hidden="true">
          <circle cx="6" cy="6" r="6" fill="var(--burgundy)"/>
          <path d="M4 3.2l1 .1.5 1.4-.7.6c.3.7.9 1.3 1.6 1.6l.6-.7 1.4.5.1 1c-.4.6-1 .9-1.6.7C5 7.9 4.1 7 3.6 5.4c-.2-.7.1-1.7.4-2.2z" fill="var(--white)"/>
        </svg>
        <span>518.677.3941</span>
      </li>
      <li class="contact-item">
        <svg class="contact-icon" viewBox="0 0 12 12" aria-hidden="true">
          <circle cx="6" cy="6" r="5.6" fill="var(--burgundy)"/>
          <g fill="none" stroke="var(--white)" stroke-width="0.7">
            <ellipse cx="6" cy="6" rx="2.2" ry="5.2"/>
            <line x1="0.6" y1="6" x2="11.4" y2="6"/>
            <line x1="1.5" y1="3.4" x2="10.5" y2="3.4"/>
            <line x1="1.5" y1="8.6" x2="10.5" y2="8.6"/>
          </g>
        </svg>
        <span>calmbriefcounsel.net</span>
      </li>
      <li class="contact-item">
        <svg class="contact-icon" viewBox="0 0 12 12" aria-hidden="true">
          <rect x="0.5" y="2.5" width="11" height="7.5" fill="var(--burgundy)"/>
          <path d="M0.8 2.8L6 6.8l5.2-4" fill="none" stroke="var(--white)" stroke-width="0.8"/>
        </svg>
        <span>marissa@calmbriefcounsel.net</span>
      </li>
      <li class="contact-item">
        <svg class="contact-icon" viewBox="0 0 12 12" aria-hidden="true">
          <circle cx="6" cy="6" r="6" fill="var(--burgundy)"/>
        </svg>
        <span>@calmbriefcounsel</span>
      </li>
    </ul>

    <div class="seal">Calm<br>Brief<br>Counsel</div>
  </section>

</main>
</body>
</html>
```